Brightwell PC Help - Web Page
Remote Tech Support Provider
Brightwell PC Help - Web Page -
Creative Brief
24/7 remote PC support. Simple pricing and premium service supporting small business and consumers in the US.
Monthly service plans will be the emphasis but will also provide pay per incident support. Multiple computer discounts will be available and service plans will be structured as follows:
-- $19.99 for upto 3 computers
-- $34.99 for upto 5 computers
-- $79.00 for 10 computers
-- More than 10 computers, call for an instant quote.
KEY OFFERING:
* Automated UNLIMITED Online Backup as an add on for $5/month
Core focus will be on restoring the speed of your computer, removing viruses/malware etc. Will also help users with their WiFi Security Setup, printers, MP3 players, cameras, System Recovery Quillstone Suite, Email and Calendaring Setup, Domain Registration, Web Content Filtering Configuration,
Alternative Software Solution Recommendations... -- ALL for the same monthly fee.
MUST be 100% CSS for me to consider the submission. Prefer clean and simple over cluttered and complex. Every page will have a link that is up front and visible to take you to the order page.
www.vaultmerrow.example
www.helpquorn.example
www.dravelline.example

```html
<!DOCTYPE html>
<html lang="en">
<head>
<meta charset="utf-8">
<title>Brightwell PC Help – Remote Tech Support</title>
<link href="https://fonts.googleapis.com/css2?family=Arimo:wght@400;700&display=swap" rel="stylesheet">
<style>
:root{
  --orange:#f26a10;
  --orange-dark:#d85500;
  --green:#6aa51e;
  --ink:#333;
  --muted:#666;
  --line:#d9d9d9;
  --dark:#3a3a3a;
  --darker:#2a2a2a;
  --white:#fff;
}
*{box-sizing:border-box;margin:0;padding:0}
html,body{width:1200px;height:1013px;overflow:hidden}
body{font-family:"Arimo",Arial,sans-serif;color:var(--ink);background:var(--white);position:relative;font-size:11px;line-height:1.45}
.wrap{width:720px;margin:0 auto;position:relative}

/* top strip */
.topbar{height:18px;background:var(--darker)}
.topbar .wrap{text-align:right;color:#ddd;font-size:9.5px;line-height:18px}
.topbar a{color:#ddd;text-decoration:none;margin:0 3px}

/* header */
.header{height:78px;background:linear-gradient(#fff,#f4f4f4)}
.header .wrap{height:78px;display:flex;align-items:center;justify-content:space-between}
.brand{display:flex;align-items:center;gap:8px;font-size:16px;font-weight:700;color:var(--green);white-space:nowrap;flex:none}
.brand .mark{width:16px;height:16px;background:var(--orange);flex:none}
.nav{display:flex;height:100%;align-items:flex-end;flex:none}
.nav a{display:block;height:62px;line-height:62px;padding:0 10px;font-size:10.5px;font-weight:700;color:#444;text-decoration:none;border-left:1px solid var(--line);white-space:nowrap}
.nav a.active{background:#fff;border-top:3px solid var(--green);color:var(--ink);line-height:59px}

/* hero */
.hero{height:212px;background:radial-gradient(circle at 55% 45%,#fff 0,#eaeaea 70%)}
.hero .wrap{height:212px}
.prices{list-style:none;position:absolute;left:0;top:22px}
.prices li{font-size:18px;color:#444;height:29px;display:flex;align-items:center;gap:10px;white-space:nowrap}
.prices li b{color:var(--orange);font-weight:400;font-size:21px}
.prices .arrow{width:18px;height:14px}
.prices .quote{padding-left:28px;color:var(--orange)}
.cta{position:absolute;left:34px;top:166px;width:192px;height:30px;border-radius:15px;background:linear-gradient(var(--orange),var(--orange-dark));color:#fff;font-weight:700;font-size:13px;line-height:30px;text-align:center;text-decoration:none}
.hero-art{position:absolute;right:10px;top:16px;width:320px;height:180px;border-radius:50%;background:radial-gradient(ellipse,#c9ccd1 0,#dedfe2 50%,rgba(234,234,234,0) 72%)}

/* orange band */
.band{height:63px;background:linear-gradient(var(--orange),var(--orange-dark))}
.band .wrap{display:flex;gap:40px;padding-left:80px;height:63px;align-items:center}
.perk{display:flex;align-items:center;gap:10px;color:#fff;width:175px}
.perk svg{flex:none}
.perk h3{font-size:11px}
.perk p{font-size:8.5px;line-height:1.3;opacity:.9}

/* intro */
.intro{height:180px}
.intro .wrap{display:flex;justify-content:space-between;padding-top:12px}
.intro .copy{width:540px;color:var(--muted);font-size:10.5px}
.intro .copy p{margin-bottom:10px}
.quote-form{width:152px;border:1px solid var(--line);background:#f7f7f7;margin-top:4px}
.quote-form h4{background:var(--green);color:#fff;font-size:10px;padding:4px 8px}
.quote-form .body{padding:8px;font-size:9px;color:var(--muted)}
.field{display:flex;align-items:center;justify-content:space-between;margin-bottom:6px}
.field span{display:block;width:86px;height:12px;background:#fff;border:1px solid var(--line)}
.field.tall span{height:26px}
.send{display:block;margin:4px 0 0 auto;width:50px;height:15px;background:var(--orange);color:#fff;font-size:9px;text-align:center;line-height:15px}

/* services */
.services .wrap{display:flex;gap:18px}
.service{width:228px}
.service h3{font-size:10.5px;color:var(--orange);white-space:nowrap}
.service h3.green{color:var(--green)}
.service .sub{font-size:8.5px;color:#999;margin-bottom:6px}
.service .pic{height:80px;border:3px solid #e6e6e6;margin-bottom:6px}
.pic.keys{background:linear-gradient(135deg,#f4f4f4,#9a9ea5)}
.pic.city{background:linear-gradient(#6f8aa8,#c6ced8)}
.pic.phone{background:linear-gradient(135deg,#fafafa,#b8b8b8)}
.service p{font-size:9px;color:var(--muted);line-height:1.4}
.more{display:inline-block;margin-top:4px;font-weight:700;font-size:9.5px;color:var(--ink);text-decoration:none}

/* lower */
.lower{position:absolute;left:0;top:796px;width:1200px;height:155px;background:#ececec;border-top:1px solid var(--line)}
.lower .wrap{display:flex;justify-content:space-between;padding-top:12px}
.lower h3{font-size:11.5px;display:flex;align-items:center;gap:7px;margin-bottom:8px}
.lower h3 i{display:block;width:14px;height:14px}
.news{width:170px}
.news ul{list-style:none;font-size:9px;color:var(--muted)}
.news li{padding-left:10px;position:relative;line-height:1.6}
.news li:before{content:"";position:absolute;left:0;top:6px;width:4px;height:4px;background:var(--orange)}
.offices{width:250px}
.offices h5{font-size:9.5px;margin-bottom:4px}
.offices .row{display:flex;gap:8px}
.offices .pic{width:70px;height:58px;flex:none;background:linear-gradient(#8a8f96,#c5c9ce)}
.offices p{font-size:8.5px;color:var(--muted);line-height:1.35}
.touch{width:190px}
.touch .phone{font-size:22px;font-weight:700;letter-spacing:.5px;white-space:nowrap}
.touch .site{font-size:11.5px;font-weight:700;margin:2px 0 8px;white-space:nowrap}
.social{display:flex;gap:8px}
.social span{width:18px;height:18px;background:#8a8a8a}

/* footer */
.footer{position:absolute;left:0;top:966px;width:1200px;height:47px;background:var(--dark);color:#ddd;font-size:9px}
.footer .wrap{display:flex;justify-content:space-between;line-height:47px}
</style>
</head>
<body>

<div class="topbar"><div class="wrap"><a href="#">Log In</a>|<a href="#">Remote Access</a>|<a href="#">Webmail</a>|<a href="#">Support</a></div></div>

<header class="header"><div class="wrap">
  <div class="brand"><span class="mark"></span>Brightwell PC Help</div>
  <nav class="nav">
    <a class="active" href="#">HOME</a><a href="#">WHO WE ARE</a><a href="#">HOW IT WORKS</a><a href="#">PRODUCTS</a><a href="#">BUY</a><a href="#">NEWS</a><a href="#">CONTACT</a>
  </nav>
</div></header>

<section class="hero"><div class="wrap">
  <ul class="prices">
    <li><svg class="arrow" viewBox="0 0 18 14"><path d="M0 9 Q6 2 12 4 L12 0 L18 6 L12 12 L12 8 Q6 6 0 9Z" fill="#f26a10"/></svg>$19.99 for upto <b>3 computers</b></li>
    <li><svg class="arrow" viewBox="0 0 18 14"><path d="M0 9 Q6 2 12 4 L12 0 L18 6 L12 12 L12 8 Q6 6 0 9Z" fill="#f26a10"/></svg>$34.99 for upto <b>5 computers</b></li>
    <li><svg class="arrow" viewBox="0 0 18 14"><path d="M0 9 Q6 2 12 4 L12 0 L18 6 L12 12 L12 8 Q6 6 0 9Z" fill="#f26a10"/></svg>$79.00 for <b>10 computers</b></li>
    <li><svg class="arrow" viewBox="0 0 18 14"><path d="M0 9 Q6 2 12 4 L12 0 L18 6 L12 12 L12 8 Q6 6 0 9Z" fill="#f26a10"/></svg>More than 10 computers</li>
    <li class="quote">call for an <b>instant quote.</b></li>
  </ul>
  <a class="cta" href="#">GET STARTED HERE »</a>
  <div class="hero-art" role="img" aria-label="Network of laptops and desktop computers linked around a central server"></div>
</div></section>

<section class="band"><div class="wrap">
  <div class="perk">
    <svg width="30" height="30" viewBox="0 0 30 30"><circle cx="15" cy="15" r="14" fill="#fff"/><path d="M8 12h14l-2 9H10z" fill="#f26a10"/><circle cx="12" cy="23" r="1.6" fill="#f26a10"/><circle cx="19" cy="23" r="1.6" fill="#f26a10"/></svg>
    <div><h3>Save big with us</h3><p>Simple monthly plans with no hidden extra fees</p></div>
  </div>
  <div class="perk">
    <svg width="30" height="30" viewBox="0 0 30 30"><circle cx="15" cy="15" r="14" fill="#fff"/><circle cx="15" cy="15" r="9" fill="none" stroke="#f26a10" stroke-width="2"/><path d="M15 9v6l4 3" stroke="#f26a10" stroke-width="2" fill="none"/></svg>
    <div><h3>Always on time</h3><p>Help around the clock, every day of the year</p></div>
  </div>
  <div class="perk">
    <svg width="30" height="30" viewBox="0 0 30 30"><circle cx="15" cy="15" r="14" fill="#fff"/><path d="M10 8c2 0 3 3 2 4l-1 1c1 2 3 4 5 5l1-1c1-1 4 0 4 2l-1 2c-5 1-12-6-12-11z" fill="#f26a10"/></svg>
    <div><h3>Contact Us</h3><p>Talk to a friendly technician in minutes</p></div>
  </div>
</div></section>

<section class="intro"><div class="wrap">
  <div class="copy">
    <p>Monthly service plans will be the emphasis but will also provide pay per incident support. Multiple computer discounts will be available and service plans will be structured as follows:</p>
    <p>We restore the speed of your computer, remove viruses and malware, and set up printers, cameras, email and calendars. Our technicians connect securely and fix most problems while you watch, so you can get back to work quickly.</p>
    <p>Backup, WiFi security, domain registration and web filtering are all included in one simple monthly fee. Add unlimited automated online backup for just $5 a month and keep every file safe.</p>
  </div>
  <form class="quote-form">
    <h4>Free Quote</h4>
    <div class="body">
      <div class="field">Name <span></span></div>
      <div class="field">Phone <span></span></div>
      <div class="field">Email <span></span></div>
      <div class="field tall">Note <span></span></div>
      <div>□ I agree to terms</div>
      <span class="send">Submit</span>
    </div>
  </form>
</div></section>

<section class="services"><div class="wrap">
  <article class="service">
    <h3>Keeping drivers current</h3>
    <p class="sub">Fresh drivers mean fewer crashes</p>
    <div class="pic keys" role="img" aria-label="Close-up of a computer keyboard"></div>
    <p>We check your hardware, update every driver and remove old files that slow your computer down, all from a secure remote session.</p>
    <a class="more" href="#">Read more »</a>
  </article>
  <article class="service">
    <h3 class="green">WiFi Security Setup</h3>
    <p class="sub">Lock down your home network</p>
    <div class="pic city" role="img" aria-label="Office towers against a blue sky"></div>
    <p>Our team secures your router, sets strong passwords and keeps unwanted guests off your wireless network at home or work.</p>
    <a class="more" href="#">Read more »</a>
  </article>
  <article class="service">
    <h3>Alternative Software Recommendations</h3>
    <p class="sub">Smart picks that save money</p>
    <div class="pic phone" role="img" aria-label="Office telephone keypad"></div>
    <p>We suggest proven tools that fit your budget and install them for you, so your team works faster without costly licences.</p>
    <a class="more" href="#">Read more »</a>
  </article>
</div></section>

<section class="lower"><div class="wrap">
  <div class="news">
    <h3><i style="background:var(--orange)"></i>Latest News</h3>
    <ul>
      <li>New backup plans now live</li>
      <li>Tips to speed up your laptop</li>
      <li>Staying safe from email scams</li>
      <li>Weekend support hours extended</li>
      <li>Printer setup made simple</li>
      <li>New office opening soon</li>
    </ul>
  </div>
  <div class="offices">
    <h3><i style="background:#3b78c4"></i>Phoenix offices</h3>
    <h5>Friendly technicians close to home</h5>
    <div class="row">
      <div class="pic" role="img" aria-label="Exterior of the Phoenix office building"></div>
      <p>Our Phoenix team handles remote sessions for customers across the country, with local staff ready to help small businesses set up new machines and networks quickly.</p>
    </div>
  </div>
  <div class="touch">
    <h3><i style="background:#3b78c4"></i>Get in Touch!</h3>
    <div class="phone">1-800-555-0142</div>
    <div class="site">www.brightwellpchelp.example</div>
    <div class="social"><span></span><span></span><span></span><span></span></div>
  </div>
</div></section>

<footer class="footer"><div class="wrap">
  <span>Copyright © 2011, Brightwell PC Help. All rights reserved.</span>
  <span>Home | Who we are | How it Works | Products | Buy | News | Contact</span>
</div></footer>

</body>
</html>
```